want business card , letter head & envelop design for my company

I want Business Card, letter head & Envelope design for my agriculture farm company.
MORVEL AGRO HOLDINGS PRIVATE LIMITED.
I have already designed logo and attached it.
Want with all format like:GIF, JPEG, JPG, PNG, PSD etc with source.
Note: All the design should be editable in Photoshop.

```html
<!DOCTYPE html>
<html lang="en">
<head>
<meta charset="utf-8">
<title>Morvel Agro Holdings – Stationery</title>
<link href="https://fonts.googleapis.com/css2?family=Montserrat:wght@600;700&family=Open+Sans:ital,wght@0,400;0,600;0,700;1,700&display=swap" rel="stylesheet">
<style>
  :root{
    --bg:#4f717b;
    --navy:#2c2a6c;
    --green:#1f7a3b;
    --ink:#2b2b2b;
    --paper:#fafafa;
    --white:#ffffff;
  }
  *{box-sizing:border-box;margin:0;padding:0}
  html,body{width:1200px;height:872px;overflow:hidden}
  body{background:var(--bg);position:relative;font-family:"Open Sans",Arial,sans-serif;color:var(--ink)}

  /* Letterhead */
  .letterhead{position:absolute;left:79px;top:109px;width:497px;height:667px;background:var(--paper);box-shadow:0 6px 18px rgba(0,0,0,.25)}
  .lh-header{position:absolute;left:0;top:12px;width:100%;height:63px;background:var(--navy)}
  .lh-brand{position:absolute;left:32px;top:7px;width:206px;height:49px;background:var(--white);display:flex;align-items:center;padding-left:10px;gap:8px}
  .brand-square{width:14px;height:14px;background:var(--green);flex:none}
  .lh-brand .brand-name{font-family:"Montserrat",sans-serif;font-weight:700;color:var(--navy);font-size:13px;line-height:1.15}
  .lh-contact{position:absolute;right:12px;top:7px;list-style:none;text-align:right;color:var(--white);font-size:12.5px;line-height:17px}
  .lh-contact li{display:flex;justify-content:flex-end;align-items:center;gap:6px}
  .dot-icon{width:12px;height:12px;border-radius:50%;background:var(--white);display:inline-block}
  .lh-body{position:absolute;left:32px;top:83px;width:436px;font-size:10.6px;line-height:15px;color:#333}
  .lh-date{margin-bottom:19px}
  .recipient-name{font-size:13px;font-weight:600;color:#222;line-height:16px}
  .lh-body p{margin-bottom:15px;text-align:left}
  .lh-address{margin:14px 0 15px}
  .sign-name{font-weight:700;font-style:italic;font-size:15px;color:#111}
  .lh-footer{position:absolute;left:0;bottom:10px;width:383px;height:30px;background:var(--navy);color:var(--white);font-size:10.5px;display:flex;align-items:center;padding-left:10px;gap:10px}
  .lh-corner{position:absolute;right:10px;bottom:10px;width:66px;height:66px;display:flex;align-items:flex-end;justify-content:flex-end}
  .corner-square{width:44px;height:44px;background:var(--green)}

  /* Business cards */
  .card{position:absolute;left:657px;width:487px;height:277px;background:var(--white);border-radius:16px;overflow:hidden;box-shadow:0 6px 18px rgba(0,0,0,.25)}
  .card-front{top:133px;display:flex;flex-direction:column;align-items:center;justify-content:center;gap:14px}
  .card-front .brand-square{width:34px;height:34px}
  .card-front .brand-name{font-family:"Montserrat",sans-serif;font-weight:700;color:var(--navy);font-size:36px;line-height:42px;text-align:center}
  .card-back{top:469px}
  .cb-brand{position:absolute;left:20px;top:60px;width:222px;text-align:center}
  .cb-brand .brand-name{font-family:"Montserrat",sans-serif;font-weight:700;color:var(--navy);font-size:23px;line-height:28px}
  .cb-divider{position:absolute;left:260px;top:82px;width:2px;height:112px;background:var(--navy)}
  .cb-person{position:absolute;left:293px;top:83px}
  .person-name{font-family:"Open Sans",sans-serif;font-weight:700;font-size:17px;color:var(--navy);line-height:20px}
  .person-title{font-size:13px;color:#333;margin-bottom:6px}
  .cb-contact{list-style:none;font-size:13px;line-height:17px;color:#222}
  .cb-contact li{display:flex;align-items:center;gap:7px}
  .cb-contact svg{width:11px;height:11px;fill:var(--green);flex:none}
  .cb-footer{position:absolute;left:0;top:240px;width:398px;height:28px;background:var(--navy);color:var(--white);font-size:12.5px;display:flex;align-items:center;padding-left:33px}
  .cb-corner{position:absolute;right:18px;bottom:9px;width:44px;height:44px;background:var(--green)}
</style>
</head>
<body>

<section class="letterhead" aria-label="Letterhead">
  <header class="lh-header">
    <div class="lh-brand">
      <span class="brand-square"></span>
      <span class="brand-name">MORVEL AGRO<br>HOLDINGS PVT. LTD</span>
    </div>
    <ul class="lh-contact">
      <li>+123 555 0147 <span class="dot-icon"></span></li>
      <li>info@morvelagro.com <span class="dot-icon"></span></li>
      <li>www.morvelagro.com <span class="dot-icon"></span></li>
    </ul>
  </header>

  <div class="lh-body">
    <div class="lh-date">January-18-2021</div>
    <div class="recipient-name">Mr, Alan Pereira</div>
    <div>President</div>
    <div class="lh-address">Brightfield Traders<br>48 Orchard Lane, Suite 6<br>Greenvale, State, 120045</div>
    <p>Dear Mr, Alan</p>
    <p>Lorem ipsum dolor sit amet, consectetur adipisicing elit, sed do eiusmod tempor incididunt ut labore et dolore magna aliqua. Ut enim ad minim veniam, quis nostrud exercitation ullamco laboris nisi ut aliquip ex ea commodo consequat. Duis aute irure dolor in reprehenderit in voluptate velit esse cillum dolore eu fugiat nulla pariatur.</p>
    <p>Lorem ipsum dolor sit amet, consectetur adipisicing elit, sed do eiusmod tempor incididunt ut labore et dolore magna aliqua. Ut enim ad minim veniam, quis nostrud exercitation ullamco laboris nisi ut aliquip ex ea commodo consequat. Duis aute irure dolor in reprehenderit in voluptate velit esse cillum dolore eu fugiat nulla pariatur.</p>
    <p>Lorem ipsum dolor sit amet, consectetur adipisicing elit, sed do eiusmod tempor incididunt ut labore et dolore magna aliqua. Ut enim ad minim veniam, quis nostrud exercitation ullamco laboris nisi ut aliquip ex ea commodo consequat. Excepteur sint occaecat cupidatat non proident, sunt in culpa qui officia deserunt mollit anim id est laborum. re et dolore magnam aliquam quaerat voluptatem.</p>
    <div>Regards</div>
    <div class="sign-name">Daniel</div>
  </div>

  <footer class="lh-footer">
    <svg width="14" height="18" viewBox="0 0 14 18" aria-hidden="true"><path d="M7 0C3.1 0 0 3.1 0 7c0 5 7 11 7 11s7-6 7-11c0-3.9-3.1-7-7-7zm0 9.5A2.5 2.5 0 1 1 7 4.5a2.5 2.5 0 0 1 0 5z" fill="#fff"/></svg>
    <span>Veldstraat 14B, 7741KP, Oosterhout, Drenthe, Netherlands</span>
  </footer>
  <div class="lh-corner"><span class="corner-square"></span></div>
</section>

<section class="card card-front" aria-label="Business card front">
  <span class="brand-square"></span>
  <div class="brand-name">MORVEL AGRO<br>HOLDINGS PVT. LTD</div>
</section>

<section class="card card-back" aria-label="Business card back">
  <div class="cb-brand"><div class="brand-name">MORVEL AGRO<br>HOLDINGS PVT. LTD</div></div>
  <div class="cb-divider"></div>
  <div class="cb-person">
    <div class="person-name">ROHAN MEHTA</div>
    <div class="person-title">General Manager</div>
    <ul class="cb-contact">
      <li><svg viewBox="0 0 12 12"><path d="M2.4 0.6 4.2 2.4 3.3 4a7 7 0 0 0 4.7 4.7l1.6-.9 1.8 1.8L10 11.4C5 11.2.8 7 .6 2z"/></svg>+123 555 0147</li>
      <li><svg viewBox="0 0 12 12"><rect x="2.5" y="0" width="7" height="12" rx="1.2"/></svg>+123 555 0147</li>
      <li><svg viewBox="0 0 12 12"><path d="M0 2h12v1.2L6 7 0 3.2zM0 4.6l6 3.8 6-3.8V10H0z"/></svg>info@morvelagro.com</li>
      <li><svg viewBox="0 0 12 12"><circle cx="6" cy="6" r="6"/></svg>www.morvelagro.com</li>
    </ul>
  </div>
  <div class="cb-footer">88 Harvest Avenue, Fresno, California 93701, United States</div>
  <div class="cb-corner"></div>
</section>

</body>
</html>
```